Copper Ridge Inquiries Letterhead

I would like to design a letterhead for a private investigation company. Our primary clients will be law firms. The business card is included below

```html
<!DOCTYPE html>
<html lang="en">
<head>
<meta charset="utf-8">
<title>Copper Ridge Inquiries Letterhead</title>
<link href="https://fonts.googleapis.com/css2?family=Montserrat:wght@400;700;800&family=Lato:wght@400;700&family=Dancing+Script:wght@500&display=swap" rel="stylesheet">
<style>
  :root {
    --navy: #1c2f5a;
    --orange: #ee5a32;
    --ink: #1b1b1b;
    --muted: #3a3a3a;
    --paper: #ffffff;
    --backdrop: #e4e4e4;
  }
  * { margin: 0; padding: 0; box-sizing: border-box; }
  html, body { width: 1200px; height: 1079px; overflow: hidden; }
  body { background: var(--backdrop); position: relative; font-family: "Lato", sans-serif; color: var(--ink); }

  .letterhead {
    position: absolute; left: 232px; top: 20px;
    width: 735px; height: 1039px;
    background: var(--paper);
    box-shadow: 0 4px 18px rgba(0,0,0,0.12);
    overflow: hidden;
  }

  .brand { position: absolute; left: 37px; top: 52px; width: 175px; text-align: center; }
  .brand-dot { width: 58px; height: 58px; border-radius: 50%; background: var(--orange); margin: 0 auto 14px; }
  .brand-name {
    font-family: "Montserrat", sans-serif; font-weight: 800; color: var(--navy);
    font-size: 21px; line-height: 1.1; letter-spacing: 0.2px;
  }

  .contact-rule { position: absolute; left: 333px; top: 94px; width: 1.5px; height: 73px; background: var(--orange); }
  .contact { position: absolute; left: 365px; top: 91px; font-family: "Montserrat", sans-serif; font-size: 12.5px; color: var(--muted); }
  .contact-line { display: flex; align-items: center; height: 18.6px; }
  .contact-line svg { width: 11px; height: 11px; margin-left: -18px; margin-right: 7px; fill: var(--orange); }
  .license { margin-top: 7px; }

  .letter { position: absolute; left: 37px; width: 661px; font-size: 14px; line-height: 17.2px; }
  .date { top: 284px; }
  .recipient { top: 320px; }
  .company { top: 372px; }
  .salutation { top: 444px; font-size: 18px; font-weight: 700; }
  .body { top: 484px; text-align: justify; line-height: 16.1px; }
  .body p { margin-bottom: 16.5px; }
  .closing { top: 781px; }
  .signature { top: 884px; font-family: "Dancing Script", cursive; font-size: 31px; line-height: 1.2; }

  .footer-band { position: absolute; left: 0; top: 1008px; width: 100%; height: 14px; display: flex; }
  .footer-band .band-orange { flex: 0 0 628px; background: var(--orange); color: #fff; font-family: "Montserrat", sans-serif; font-size: 12px; line-height: 14px; padding-left: 207px; white-space: nowrap; }
  .footer-band .band-navy { flex: 1; background: var(--navy); }
  .footer-mark { position: absolute; left: 621px; top: 1001px; width: 28px; height: 28px; border-radius: 50%; background: var(--paper); border: 2px solid var(--navy); }
</style>
</head>
<body>
  <main class="letterhead">
    <header>
      <div class="brand">
        <div class="brand-dot"></div>
        <div class="brand-name">COPPER RIDGE<br>INQUIRIES</div>
      </div>
      <div class="contact-rule"></div>
      <div class="contact">
        <div class="contact-line">
          <svg viewBox="0 0 12 12"><path d="M6 0a4.2 4.2 0 0 0-4.2 4.2C1.8 7.4 6 12 6 12s4.2-4.6 4.2-7.8A4.2 4.2 0 0 0 6 0zm0 6a1.8 1.8 0 1 1 0-3.6A1.8 1.8 0 0 1 6 6z"/></svg>
          MARLOW SPRINGS, TX
        </div>
        <div class="contact-line">
          <svg viewBox="0 0 12 12"><path d="M1 4.5C1 3 3 2 6 2s5 1 5 2.5v1H8.5V4.3C7.7 4 4.3 4 3.5 4.3v1.2H1zM2.5 6.5h7l1 4h-9z"/></svg>
          555.214.7730
        </div>
        <div class="contact-line">
          <svg viewBox="0 0 12 12"><path d="M6 1a5 5 0 1 0 2.6 9.3l-.5-.9A4 4 0 1 1 10 6v.6c0 .6-.4 1-.9 1s-.9-.4-.9-1V3.5h-1v.4A2.5 2.5 0 1 0 7.5 8a1.9 1.9 0 0 0 3.5-1.4V6A5 5 0 0 0 6 1zm0 6.5A1.5 1.5 0 1 1 6 4.5a1.5 1.5 0 0 1 0 3z"/></svg>
          DANA@COPPERRIDGEINQUIRIES.COM
        </div>
        <div class="license">LICENSE NO. 04729163</div>
      </div>
    </header>

    <div class="letter date">January-03-2020</div>
    <div class="letter recipient">Mr, Daniel Reyes<br>President</div>
    <div class="letter company">Harbor Lane Group<br>123 Street Name, Suite# 10<br>City, State, 120023</div>
    <div class="letter salutation">Dear Mr, Daniel</div>
    <div class="letter body">
      <p>Lorem ipsum dolor sit amet, consectetur adipiscing elit, sed do eiusmod tempor incididunt ut labore et dolore magna aliqua. Ut enim ad minim veniam, quis nostrud exercitation ullamco laboris nisi ut aliquip ex ea commodo consequat. Duis aute irure dolor in reprehenderit in voluptate velit esse cillum dolore eu fugiat nulla pariatur.</p>
      <p>Lorem ipsum dolor sit amet, consectetur adipiscing elit, sed do eiusmod tempor incididunt ut labore et dolore magna aliqua. Ut enim ad minim veniam, quis nostrud exercitation ullamco laboris nisi ut aliquip ex ea commodo consequat. Duis aute irure dolor in reprehenderit in voluptate velit esse cillum dolore eu fugiat nulla pariatur.</p>
      <p>Lorem ipsum dolor sit amet, consectetur adipiscing elit, sed do eiusmod tempor incididunt ut labore et dolore magna aliqua. Ut enim ad minim veniam, quis nostrud exercitation ullamco laboris nisi ut aliquip ex ea commodo consequat.</p>
      <p>Excepteur sint occaecat cupidatat non proident, sunt in culpa qui officia deserunt mollit anim id est laborum. re et dolore magnam aliquam quaerat voluptatem.</p>
    </div>
    <div class="letter closing">Regards</div>
    <div class="letter signature">Elena Ward</div>

    <footer class="footer-band">
      <div class="band-orange">OVER 20 YEARS OF INVESTIGATIVE EXPERINCE</div>
      <div class="band-navy"></div>
    </footer>
    <div class="footer-mark"></div>
  </main>
</body>
</html>
```